Meadowlark Counseling Business Card Design Project

I am starting a new business that provides counseling and coaching services to individuals and couples. These individuals are people looking to "transform" or grow in the personal lives. The design should convey trust, intimacy, hope, growth. It should be professional, elegant.
Contact information
Name: Dana R. Whitcombe
Title: Counselor and Life Coach
Slogan: Steady Care. Growing Together.
address: 47310 County Road 9, Suite 410
Plymouth, MN 55490
Phone: 763-555-0184
Email: dana@meadowlark-cx.example
website: www.meadowlark-cx.example
Back side of card should have bullets:
Individual counseling
Relationship counseling
Life Coaching for Teens and Adults
Group Workshops

```html
<!DOCTYPE html>
<html lang="en">
<head>
<meta charset="utf-8">
<title>Meadowlark Counseling – Business Card</title>
<link href="https://fonts.googleapis.com/css2?family=Marcellus+SC&family=Dancing+Script:wght@500&display=swap" rel="stylesheet">
<style>
  :root {
    --page-bg: #e9e6e2;
    --card-white: #f7f7f6;
    --panel-blue: #1f86c4;
    --panel-blue-light: #3b9bd3;
    --ink-blue: #2b6ea6;
    --ink-white: #ffffff;
    --rule: rgba(255,255,255,0.75);
    --bullet: #d9dde2;
  }
  * { margin: 0; padding: 0; box-sizing: border-box; }
  html, body { width: 1200px; height: 970px; overflow: hidden; }
  body {
    background: var(--page-bg);
    font-family: "Marcellus SC", serif;
    position: relative;
  }
  .card {
    position: absolute;
    left: 198px;
    width: 828px;
    height: 458px;
    display: flex;
    box-shadow: 0 2px 8px rgba(0,0,0,0.25);
  }
  .card--front { top: 17px; }
  .card--back { top: 495px; }

  .brand-side {
    background: var(--card-white);
    display: flex;
    flex-direction: column;
    align-items: center;
    justify-content: center;
    gap: 22px;
  }
  .card--front .brand-side { width: 412px; }
  .card--back .brand-side { width: 416px; }
  .brand-mark {
    width: 46px; height: 46px;
    border-radius: 50%;
    background: var(--ink-blue);
  }
  .brand-name {
    color: var(--ink-blue);
    font-size: 31px;
    letter-spacing: 1px;
    text-align: center;
    line-height: 1.2;
  }

  .info-panel {
    flex: 1;
    background: linear-gradient(160deg, var(--panel-blue-light) 0%, var(--panel-blue) 60%);
    color: var(--ink-white);
    position: relative;
  }
  .person-name {
    position: absolute; left: 52px; top: 88px;
    font-size: 23px; letter-spacing: 1.5px;
  }
  .person-rule {
    position: absolute; left: 52px; right: 0; top: 121px;
    height: 1px; background: var(--rule);
  }
  .person-title {
    position: absolute; left: 52px; top: 124px;
    font-size: 23px; letter-spacing: 1px;
  }
  .address {
    position: absolute; left: 52px; top: 217px;
    font-size: 21px; line-height: 26px; letter-spacing: 0.5px;
    font-style: normal;
  }
  .contact-list {
    position: absolute; left: 52px; top: 285px;
    list-style: none;
  }
  .contact-list li {
    display: flex; align-items: center; gap: 14px;
    height: 29px; font-size: 15px; letter-spacing: 0.8px;
  }
  .contact-list svg { width: 17px; height: 17px; flex: none; }

  .services-panel {
    width: 412px;
    background: linear-gradient(160deg, var(--panel-blue) 0%, var(--panel-blue-light) 100%);
    color: var(--ink-white);
    position: relative;
  }
  .service-list {
    position: absolute; left: 26px; top: 130px;
    list-style: none;
  }
  .service-list li {
    display: flex; align-items: center; gap: 10px;
    height: 46px; font-size: 23px; letter-spacing: 0.8px;
  }
  .service-list li.small { font-size: 19px; }
  .service-list li::before {
    content: ""; width: 10px; height: 10px; border-radius: 50%;
    background: var(--bullet);
  }
  .slogan-rule {
    position: absolute; left: 26px; right: 26px; top: 328px;
    height: 1px; background: var(--rule);
  }
  .slogan {
    position: absolute; left: 30px; top: 336px;
    font-family: "Dancing Script", cursive;
    font-size: 26px; font-style: normal;
  }
</style>
</head>
<body>
  <section class="card card--front">
    <div class="brand-side">
      <div class="brand-mark"></div>
      <div class="brand-name">Meadowlark Counseling</div>
    </div>
    <div class="info-panel">
      <div class="person-name">Dana R. Whitcombe</div>
      <div class="person-rule"></div>
      <div class="person-title">Counselor and Life Coach</div>
      <address class="address">47310 County Road 9, Suite 410<br>Plymouth, MN 55490</address>
      <ul class="contact-list">
        <li>
          <svg viewBox="0 0 24 24" fill="none" stroke="#fff" stroke-width="2.6" stroke-linecap="round"><path d="M18 4 C10 4 5 10 6 20"/><path d="M16 3 l4 3"/><path d="M4 18 l4 3"/></svg>
          763-555-0184
        </li>
        <li>
          <svg viewBox="0 0 24 24" fill="none" stroke="#fff" stroke-width="2"><rect x="2" y="5" width="20" height="14"/><path d="M2 5 l10 8 l10 -8"/></svg>
          dana@meadowlark-cx.example
        </li>
        <li>
          <svg viewBox="0 0 24 24" fill="none" stroke="#fff" stroke-width="1.8"><circle cx="12" cy="12" r="10"/><ellipse cx="12" cy="12" rx="4.5" ry="10"/><path d="M2 12 h20 M4 7 h16 M4 17 h16"/></svg>
          www.meadowlark-cx.example
        </li>
      </ul>
    </div>
  </section>

  <section class="card card--back">
    <div class="services-panel">
      <ul class="service-list">
        <li>Individual counseling</li>
        <li>Relationship counseling</li>
        <li>group workshops</li>
        <li class="small">Life Coaching for Teens &amp; Adults</li>
      </ul>
      <div class="slogan-rule"></div>
      <p class="slogan">Steady Care. Growing Together.</p>
    </div>
    <div class="brand-side">
      <div class="brand-mark"></div>
      <div class="brand-name">Meadowlark Counseling</div>
    </div>
  </section>
</body>
</html>
```